Lanternfield CD Cover

Design for the digital booklet electronic self release of a full length music recording. Original photography has been completed and chosen (attached here). The font and its positioning will be very important. I'm fairly confident it'll work best with the picture taking up the entire cover, but feel free to play around with its size (even multiple versions of the picture) if you want to think outside the box and can make it work.

The artist name is 'Lanternfield' and the name of the recording is 'Under Copper Rain.' These need to appear on the cover.

Key moods are sombre, stylish, mysterious and subtle. And unusual and original, without being in any way pretentious.

Here are some examples of what I think are interesting or decent photo based covers with text Feel free to be imaginative and not obvious so no reason to copy these:

http://www.tunevaultmag.example/photos/40213/the-30-best-most-beautiful-album-covers-of-2013

http://en.wikiloreo.example/wiki/File:Paper_Herons_Velvet_Harbour_album_cover.jpg

http://en.wikiloreo.example/wiki/Lanterns_%28Driftmere_album%29

Industry/Entity Type

Digital

```html
<!DOCTYPE html>
<html lang="en">
<head>
<meta charset="utf-8">
<title>Lanternfield — Under Copper Rain</title>
<link rel="stylesheet" href="https://fonts.googleapis.com/css2?family=Fira+Sans+Extra+Condensed:wght@300;600&display=swap">
<style>
  :root {
    --sky-glow: #f7e3c2;
    --sky-light: #efd3a6;
    --sky-mid: #e6bf8a;
    --sky-warm: #deb27a;
    --haze: #c9a070;
    --brick-light: #7a5633;
    --brick-mid: #63432a;
    --brick-dark: #4a321f;
    --title-ink: #4a3115;
    --record-ink: #5a3d1d;
    --rule-ink: #6b4c2b;
  }
  html, body {
    margin: 0;
    padding: 0;
    width: 1200px;
    height: 1200px;
    overflow: hidden;
    background: var(--sky-mid);
  }
  .cover {
    position: relative;
    width: 1200px;
    height: 1200px;
    overflow: hidden;
  }
  .cover-photo {
    position: absolute;
    inset: 0;
    background:
      radial-gradient(ellipse 55% 40% at 22% 18%, var(--sky-glow) 0%, rgba(247,227,194,0) 100%),
      radial-gradient(ellipse 40% 22% at 38% 52%, rgba(240,222,196,0.7) 0%, rgba(240,222,196,0) 100%),
      linear-gradient(177deg,
        var(--sky-light) 0%,
        var(--sky-mid) 30%,
        var(--sky-warm) 48%,
        var(--haze) 54%,
        var(--brick-light) 61%,
        var(--brick-mid) 78%,
        var(--brick-dark) 100%);
  }
  .cover-title {
    position: absolute;
    top: 102px;
    right: 96px;
    margin: 0;
    display: flex;
    align-items: center;
    gap: 9px;
    font-family: "Fira Sans Extra Condensed", "Arial Narrow", sans-serif;
    font-size: 27px;
    line-height: 1;
    white-space: nowrap;
  }
  .artist-name {
    font-weight: 600;
    color: var(--title-ink);
  }
  .title-divider {
    display: inline-block;
    width: 1.5px;
    height: 28px;
    background: var(--rule-ink);
  }
  .record-name {
    font-weight: 300;
    color: var(--record-ink);
  }
</style>
</head>
<body>
  <main class="cover">
    <div class="cover-photo" role="img" aria-label="Full-bleed sepia photograph: large satellite dishes rising behind angled brick rooftop walls under an overcast amber sky"></div>
    <h1 class="cover-title">
      <span class="artist-name">lanternfield</span>
      <span class="title-divider" aria-hidden="true"></span>
      <span class="record-name">under copper rain</span>
    </h1>
  </main>
</body>
</html>
```